Dorsey K. Wendell Business Card

We need a business card for our company Dorsey K. Wendell Heating & Plumbing to be distributed to potential customers. It should follow the color scheme of our logo and have a modern upscale and masculine look.

The logo is attached and the info below should also be included:

5187 W. Cedar Brook Rd.
Brenford, PA 17538

Russell T. Wendell
(717) 592-0817
russelltwendell@fernmail.net
dorseykwendell.net
PA #093148

Industry/Entity Type

Business

Contact Information for Business Card

5187 W. Cedar Brook Rd.
Brenford, PA 17538

Russell T. Wendell
(717) 592-0817
russelltwendell@fernmail.net
dorseykwendell.net
PA #093148

Colors

Designer to choose colors to be used in the design.

Requirements
Must have
• Information above included

```html
<!DOCTYPE html>
<html lang="en">
<head>
<meta charset="utf-8">
<title>Dorsey K. Wendell Business Card</title>
<link rel="stylesheet" href="https://fonts.googleapis.com/css2?family=Exo+2:wght@400;600;700&family=Questrial&display=swap">
<style>
  :root {
    --brand-blue: #1f5ca4;
    --brand-green: #8cc43f;
    --ink: #333333;
    --paper: #f7f7f5;
    --backdrop: #e2e2e2;
  }
  * { box-sizing: border-box; margin: 0; padding: 0; }
  html, body { width: 1200px; height: 1050px; overflow: hidden; }
  body {
    background: var(--backdrop);
    position: relative;
    font-family: "Questrial", sans-serif;
  }
  .card {
    position: absolute;
    left: 170px;
    width: 860px;
    height: 492px;
    overflow: hidden;
  }
  .card--front { top: 25px; background: var(--paper); }
  .card--back { top: 533px; background: var(--brand-blue); }

  /* wordmark */
  .wordmark {
    position: absolute;
    display: flex;
    align-items: center;
    gap: 12px;
  }
  .wordmark__square { width: 40px; height: 40px; background: var(--brand-blue); flex: none; }
  .wordmark__name {
    font-family: "Exo 2", sans-serif;
    font-weight: 700;
    font-size: 22px;
    line-height: 1.1;
    letter-spacing: 0.5px;
    color: var(--brand-blue);
  }
  .card--front .wordmark { left: 58px; top: 74px; }

  /* front */
  .name-band {
    position: absolute;
    left: 511px; top: 255px;
    width: 349px; height: 42px;
    background: var(--brand-blue);
    border-left: 6px solid var(--brand-green);
    color: #fff;
    font-family: "Exo 2", sans-serif;
    font-weight: 700;
    font-size: 25px;
    letter-spacing: 1px;
    text-align: right;
    padding-right: 48px;
    line-height: 42px;
  }
  .licence {
    position: absolute;
    right: 48px; top: 307px;
    font-size: 19px; letter-spacing: 1.5px;
    color: var(--brand-blue);
  }
  .contact {
    position: absolute;
    top: 400px;
    font-size: 19px;
    line-height: 22px;
    letter-spacing: 1px;
    color: var(--ink);
  }
  .contact--address { left: 64px; }
  .contact--reach { right: 48px; text-align: right; }
  .rule {
    position: absolute;
    left: 0; top: 471px;
    width: 528px; height: 3px;
    background: var(--brand-blue);
  }
  .website {
    position: absolute;
    font-size: 19px; letter-spacing: 1.2px;
  }
  .card--front .website { right: 48px; top: 459px; color: var(--brand-blue); }

  /* back */
  .tagline-band {
    position: absolute;
    left: 0; top: 339px;
    width: 403px; height: 96px;
    background: #ffffff;
    padding: 16px 0 0 46px;
    font-family: "Exo 2", sans-serif;
    font-size: 23px;
    line-height: 29px;
    letter-spacing: 0.5px;
    color: var(--brand-blue);
  }
  .card--back .wordmark { right: 42px; top: 350px; gap: 14px; }
  .card--back .wordmark__square { width: 22px; height: 22px; background: var(--brand-green); }
  .card--back .wordmark__name { color: #ffffff; font-size: 31px; }
  .card--back .website { right: 42px; top: 450px; color: #ffffff; font-size: 21px; }
</style>
</head>
<body>
  <section class="card card--front" aria-label="Business card front">
    <div class="wordmark">
      <span class="wordmark__square"></span>
      <span class="wordmark__name">DORSEY K. WENDELL<br>HEATING &amp; PLUMBING</span>
    </div>
    <div class="name-band">Russell T. Wendell</div>
    <div class="licence">PA #093148</div>
    <div class="contact contact--address">5187 W. Cedar Brook Rd.<br>Brenford, PA 17538</div>
    <div class="contact contact--reach">(717) 592-0817<br>russelltwendell@fernmail.net</div>
    <div class="rule"></div>
    <div class="website">www.dorseykwendell.net</div>
  </section>

  <section class="card card--back" aria-label="Business card back">
    <div class="tagline-band">serving Brenford and the<br>nearby valley since 1991</div>
    <div class="wordmark">
      <span class="wordmark__square"></span>
      <span class="wordmark__name">DORSEY K. WENDELL<br>HEATING &amp; PLUMBING</span>
    </div>
    <div class="website">www.dorseykwendell.net</div>
  </section>
</body>
</html>
```